Brambury Logistics

Create a modern, simple, Elegant business card design for my business.

Services: Tamo Trucks, Transport, Contract Logistics,

Industry/Entity Type

Business

Contact Information for Business Card

Include all details same as old card plus new website address: www.bramburylogistics.com.au

Requirements
Must have
• Similar colors to Logo.

```html
<!DOCTYPE html>
<html lang="en">
<head>
<meta charset="utf-8">
<title>Brambury Logistics – Business Card</title>
<link rel="stylesheet" href="https://fonts.googleapis.com/css2?family=Roboto:wght@400;500&display=swap">
<style>
  :root {
    --bg: #ecebe8;
    --card: #ffffff;
    --card-shade: #f1f2f3;
    --blue: #1a9cc9;
    --blue-light: #2bbad8;
    --grey-line: #7d7f82;
    --ink: #2a2b2d;
    --brand: #1f8fbf;
  }
  * { margin: 0; padding: 0; box-sizing: border-box; }
  html, body { width: 1200px; height: 858px; overflow: hidden; }
  body {
    background: var(--bg);
    font-family: "Roboto", Arial, sans-serif;
    color: var(--ink);
    display: flex;
    align-items: center;
    justify-content: center;
    gap: 40px;
  }
  .card {
    position: relative;
    width: 560px;
    height: 320px;
    background: radial-gradient(ellipse at 55% 40%, var(--card) 40%, var(--card-shade) 100%);
    box-shadow: 0 6px 18px rgba(0,0,0,0.18);
    overflow: hidden;
  }
  .card__wave { position: absolute; inset: 0; width: 100%; height: 100%; }
  .brand {
    display: flex;
    align-items: center;
    gap: 10px;
    font-weight: 500;
    color: var(--brand);
    white-space: nowrap;
  }
  .brand__mark {
    width: 14px; height: 14px;
    background: var(--brand);
  }
  .card--front .brand {
    position: absolute;
    left: 40px; top: 46px;
    font-size: 26px;
  }
  .contacts {
    position: absolute;
    right: 34px; top: 120px;
    list-style: none;
    display: flex;
    flex-direction: column;
    gap: 12px;
    align-items: flex-end;
    font-size: 15px;
  }
  .contacts li { display: flex; align-items: center; gap: 10px; }
  .contacts__icon {
    width: 20px; height: 20px;
    background: var(--blue);
    display: flex; align-items: center; justify-content: center;
  }
  .contacts__icon svg { width: 13px; height: 13px; }
  .card--back {
    display: flex;
    flex-direction: column;
    align-items: center;
    justify-content: center;
    gap: 26px;
  }
  .card--back .brand { font-size: 34px; }
  .services { font-size: 17px; letter-spacing: 0.2px; }
</style>
</head>
<body>
  <section class="card card--front">
    <svg class="card__wave" viewBox="0 0 560 320" preserveAspectRatio="none" aria-hidden="true">
      <defs>
        <linearGradient id="band" x1="0" y1="0" x2="1" y2="0">
          <stop offset="0" stop-color="#1a94c4"/>
          <stop offset="1" stop-color="#2cbdd9"/>
        </linearGradient>
      </defs>
      <path d="M0,178 Q210,300 560,292 L560,320 L0,320 Z" fill="url(#band)"/>
      <path d="M0,160 Q220,290 560,284" fill="none" stroke="var(--grey-line)" stroke-width="7"/>
    </svg>
    <div class="brand"><span class="brand__mark"></span>Brambury Logistics</div>
    <ul class="contacts">
      <li>0400 555 012
        <span class="contacts__icon"><svg viewBox="0 0 24 24"><path fill="#fff" d="M6.6 10.8a15 15 0 0 0 6.6 6.6l2.2-2.2c.3-.3.7-.4 1-.2 1.1.4 2.3.6 3.6.6.6 0 1 .4 1 1V20c0 .6-.4 1-1 1A17 17 0 0 1 3 4c0-.6.4-1 1-1h3.5c.6 0 1 .4 1 1 0 1.3.2 2.5.6 3.6.1.3 0 .7-.2 1z"/></svg></span>
      </li>
      <li>reno@bramburylogistics.com.au
        <span class="contacts__icon"><svg viewBox="0 0 24 24"><rect x="3" y="6" width="18" height="12" fill="none" stroke="#fff" stroke-width="2"/><path d="M3 6l9 7 9-7" fill="none" stroke="#fff" stroke-width="2"/></svg></span>
      </li>
      <li>www.bramburylogistics.com.au
        <span class="contacts__icon"><svg viewBox="0 0 24 24"><g fill="none" stroke="#fff" stroke-width="1.8"><circle cx="12" cy="12" r="9"/><ellipse cx="12" cy="12" rx="4" ry="9"/><path d="M3 12h18M5 7h14M5 17h14"/></g></svg></span>
      </li>
    </ul>
  </section>

  <section class="card card--back">
    <div class="brand"><span class="brand__mark"></span>Brambury Logistics</div>
    <p class="services">Tamo Trucks | Transport | Contract Logistics</p>
  </section>
</body>
</html>
```